Harbor Nightclub

Nightclub flyer., digital single sided, for KV and PX. I included samples of some previous flyers we've used. Sample Info:
HARBOR
FRIDAYS
FRI MAY 1 2020
DJ VORTAN (club floor)
DJ RUZO & DJ TAV (residents on the lounge floor)
4217 Marlow Avenue Sacramento
www.harborvenuehall.example for list/VIP inquiries

Target Market(s)

Upscale top 40 crowd but want some cool and artsy like the examples included.

Font styles to use
Sans Serif

Requirements
Must have
• Harbor Logo
Nice to have
• Would be nice if the flyer can be incorporated later with DJ photos (sometimes we will add dj photos to pixagram etc). Would like a big city type of feel.
Should not have
• Nothing too sexual.

```html
<!DOCTYPE html>
<html lang="en">
<head>
<meta charset="utf-8">
<title>Harbor Nightclub – Friday Flyers</title>
<link rel="stylesheet" href="https://fonts.googleapis.com/css2?family=Montserrat:wght@300;400;600;800;900&display=swap">
<style>
  :root {
    --page-bg: #f1f1f1;
    --night-deep: #0b1553;
    --night-mid: #1c2fa8;
    --night-glow: #3a3fd0;
    --bubble-pink: #d04bd8;
    --signal-red: #ff1f3a;
    --ink-white: #ffffff;
    --shadow-cyan: #28d4ff;
    --photo-tone: #2a2440;
  }
  * { margin: 0; padding: 0; box-sizing: border-box; }
  html, body { width: 1200px; height: 1000px; overflow: hidden; }
  body {
    background: var(--page-bg);
    font-family: "Montserrat", Arial, sans-serif;
    color: var(--ink-white);
    position: relative;
  }
  .flyer {
    position: absolute;
    top: 168px;
    width: 557px;
    height: 697px;
    overflow: hidden;
    background:
      radial-gradient(circle at 28% 38%, var(--night-glow) 0%, var(--night-mid) 30%, transparent 62%),
      radial-gradient(circle at 92% 68%, rgba(208,75,216,0.55) 0%, rgba(208,75,216,0.15) 22%, transparent 34%),
      radial-gradient(circle at 70% 0%, rgba(208,75,216,0.35) 0%, transparent 22%),
      linear-gradient(160deg, var(--night-mid) 0%, var(--night-deep) 70%, #0a1140 100%);
    box-shadow: 0 14px 18px rgba(0,0,0,0.12);
  }
  .flyer--lineup { left: 20px; }
  .flyer--feature { left: 617px; }

  .backdrop-art { position: absolute; inset: 0; }

  .brand {
    position: absolute;
    left: 404px;
    top: 36px;
    width: 140px;
    text-align: center;
  }
  .brand__dot {
    display: block;
    width: 46px;
    height: 46px;
    margin: 0 auto 6px;
    border-radius: 50%;
    background: var(--ink-white);
  }
  .brand__name {
    font-weight: 400;
    font-size: 24px;
    letter-spacing: 1px;
    color: var(--ink-white);
  }

  .headline {
    position: absolute;
    left: 36px;
    top: 216px;
    font-weight: 900;
    font-size: 99px;
    line-height: 1;
    letter-spacing: 15px;
    color: var(--ink-white);
    text-shadow: 5px 3px 0 var(--signal-red), -2px 0 0 var(--shadow-cyan);
  }

  .event-info {
    position: absolute;
    left: 36px;
    top: 314px;
    display: flex;
    align-items: center;
  }
  .event-info__date {
    font-weight: 300;
    font-size: 29px;
    letter-spacing: 1px;
  }
  .event-info__rule {
    width: 2px;
    height: 34px;
    background: var(--ink-white);
    margin: 0 10px 0 16px;
  }
  .event-info__place {
    font-size: 12px;
    line-height: 1.3;
    font-weight: 400;
  }

  .lineup { position: absolute; left: 36px; }
  .lineup__floor {
    font-size: 15px;
    font-weight: 400;
    color: var(--signal-red);
    line-height: 1.2;
  }
  .lineup__djs {
    font-size: 23px;
    font-weight: 800;
    letter-spacing: 0.5px;
    line-height: 1.2;
  }

  .flyer--lineup .lineup--club { top: 414px; }
  .flyer--lineup .lineup--lounge { top: 482px; }
  .flyer--feature .lineup--lounge { top: 432px; }

  .feature-arrow {
    position: absolute;
    left: 283px;
    top: 440px;
    width: 50px;
    height: 48px;
  }

  .dj-photo {
    position: absolute;
    left: 383px;
    top: 322px;
    width: 174px;
    height: 312px;
    border-radius: 90px 0 0 90px;
    background: linear-gradient(180deg, #6b5a78 0%, var(--photo-tone) 45%, #141222 100%);
  }

  .inquiries {
    position: absolute;
    left: 0;
    width: 100%;
    top: 640px;
    text-align: center;
  }
  .inquiries__label {
    font-weight: 800;
    font-size: 15px;
    letter-spacing: 0.5px;
    margin-left: 8px;
  }
  .inquiries__url {
    font-weight: 400;
    font-size: 14px;
    letter-spacing: 1px;
    color: var(--signal-red);
    margin-left: 8px;
  }
</style>
</head>
<body>

  <section class="flyer flyer--lineup" aria-label="Friday lineup flyer">
    <div class="backdrop-art" role="img" aria-label="Abstract backdrop of glowing blue and pink bubbles"></div>

    <div class="brand">
      <span class="brand__dot"></span>
      <div class="brand__name">HARBOR</div>
    </div>

    <h1 class="headline">FRIDAY</h1>

    <div class="event-info">
      <span class="event-info__date">MAY 1 2020</span>
      <span class="event-info__rule"></span>
      <span class="event-info__place">4217 MARLOW AVE.<br>SACRAMENTO</span>
    </div>

    <div class="lineup lineup--club">
      <p class="lineup__floor">club floor</p>
      <p class="lineup__djs">DJ VORTAN</p>
    </div>
    <div class="lineup lineup--lounge">
      <p class="lineup__floor">the lounge floor residents</p>
      <p class="lineup__djs">DJ RUZO + DJ TAV</p>
    </div>

    <div class="inquiries">
      <p class="inquiries__label">FOR LIST/ VIP INQUIRIES</p>
      <p class="inquiries__url">www.harborvenuehall.example</p>
    </div>
  </section>

  <section class="flyer flyer--feature" aria-label="Friday featured DJ flyer">
    <div class="backdrop-art" role="img" aria-label="Abstract backdrop of glowing blue and pink bubbles"></div>

    <div class="brand">
      <span class="brand__dot"></span>
      <div class="brand__name">HARBOR</div>
    </div>

    <h1 class="headline">FRIDAY</h1>

    <div class="event-info">
      <span class="event-info__date">MAY 1 2020</span>
      <span class="event-info__rule"></span>
      <span class="event-info__place">4217 MARLOW AVE.<br>SACRAMENTO</span>
    </div>

    <div class="lineup lineup--lounge">
      <p class="lineup__floor">the lounge floor residents</p>
      <p class="lineup__djs">DJ RUZO</p>
    </div>

    <svg class="feature-arrow" viewBox="0 0 50 48" aria-hidden="true">
      <g fill="none" stroke-width="5" stroke-linecap="square">
        <polyline points="7,6 24,24 7,42" stroke="var(--signal-red)" transform="translate(2,1)"/>
        <polyline points="24,6 41,24 24,42" stroke="var(--signal-red)" transform="translate(2,1)"/>
        <polyline points="7,6 24,24 7,42" stroke="var(--ink-white)"/>
        <polyline points="24,6 41,24 24,42" stroke="var(--ink-white)"/>
      </g>
    </svg>

    <div class="dj-photo" role="img" aria-label="Photo of the featured resident DJ inside a glowing bubble"></div>

    <div class="inquiries">
      <p class="inquiries__label">FOR LIST/ VIP INQUIRIES</p>
      <p class="inquiries__url">www.harborvenuehall.example</p>
    </div>
  </section>

</body>
</html>
```